Holiday Let Property Management Service and Website. We manage properties for holiday letting

We want a stylish business card that reflects our brand.
*** UPDATE *** PLEASE USE THE RECTANGULAR ORANGE COLOUR SWIPE PROVIDED IN THE DROP BOX FOR THE BSINESS CARD COLOUR.***
Please view the site: www.lodgewell.com.au
Obviously, we want to use the same logo font from our site for the card design.
We want to have the name "Lodgewell" right across the front in white and an orange background colour that matches the orange on our website or a brighter fresher looking orange .
We'd like to have the details on the back similar to what I've shown below but obviously with some more aesthetic added and better positioning than I have provided.
Same colours as the front. white writing and orange background. Once we have the design we'd like the font to be raised and the finish to be a low sheen. Quality thickness and finishes.
---------------------------------------------------------------------------
(Rough idea of writing details on back of card but open to nicer repositioning)

LODGEWELL
Holiday Let Management & Consulting Specialists

Marta Van Kerr Owen Brisk
Principal Director
0492637058 0487350216

email: enquiries@lodgewell.com.au
www.lodgewell.com.au

--------------------------------------------------------------------------

Target Market(s)

Property owners who may want to convert to holiday letting and people seeking holiday accommodation.

Industry/Entity Type

Tourism

Contact Information for Business Card

(Front of card) To have "Lodgewell" to stretch across the card in white writing the same font as our website home page. (discreetly including the logo TM if possible)

------------------------------------------------------------------------------------------------
(Back of card)

LODGEWELL
Holiday Let Consultants & Management Specialists

Marta Van Kerr Owen Brisk
Principal Director
0492637058 0487350216

www.lodgewell.com.au

-----------------------------------------------------------------------------------------------

Font styles to use
Other font styles liked:
• something similar or complimentary to our logo font please

Requirements
Must have
• The same font for our logo name and close to the same colour orange as the orange footer on our website. (if you can make it pop more without going too far away from it that would be great.)
• Orange background front and back with white font.
• *** UPDATE *** PLEASE USE THE RECTANGULAR ORANGE COLOUR SWIPE PROVIDED IN THE DROP BOX FOR THE BSINESS CARD COLOUR.***
Nice to have
• Great symmetry and aesthetics
Should not have
• Any other writing except our brand name (Lodgewell) on the front of the card and a small, discreet trade mark (TM)

```html
<!DOCTYPE html>
<html lang="en">
<head>
<meta charset="utf-8">
<title>Lodgewell — Business Card</title>
<link href="https://fonts.googleapis.com/css2?family=Montserrat:wght@300;400;700&display=swap" rel="stylesheet">
<style>
  :root {
    --backdrop: #3b3b3b;
    --orange-light: #ef9444;
    --orange-deep: #d47a2e;
    --ink: #ffffff;
    --rule: rgba(255, 255, 255, 0.85);
  }
  * { box-sizing: border-box; margin: 0; padding: 0; }
  html, body {
    width: 1200px;
    height: 800px;
    overflow: hidden;
    background: var(--backdrop);
    font-family: "Montserrat", Arial, sans-serif;
    color: var(--ink);
  }
  .sheet {
    width: 1200px;
    height: 800px;
    display: flex;
    flex-direction: column;
    align-items: center;
    justify-content: center;
    gap: 36px;
  }
  .card {
    position: relative;
    width: 620px;
    height: 354px;
    background: linear-gradient(135deg, var(--orange-light) 0%, var(--orange-deep) 100%);
    box-shadow: 0 6px 18px rgba(0, 0, 0, 0.35);
    overflow: hidden;
  }

  /* Front */
  .card-front {
    display: flex;
    align-items: center;
    justify-content: center;
  }
  .front-wordmark {
    font-weight: 700;
    font-size: 84px;
    letter-spacing: -2px;
    line-height: 1;
  }
  .trademark {
    font-weight: 700;
    font-size: 14px;
    vertical-align: top;
    position: relative;
    top: 2px;
    margin-left: 2px;
    letter-spacing: 0;
  }

  /* Back */
  .card-back { padding: 44px 48px 36px; }
  .brand-row {
    display: flex;
    align-items: center;
    gap: 14px;
  }
  .brand-square {
    width: 46px;
    height: 46px;
    background: var(--ink);
    flex: none;
  }
  .brand-text { display: flex; flex-direction: column; }
  .back-wordmark {
    font-weight: 700;
    font-size: 46px;
    letter-spacing: -1px;
    line-height: 1;
  }
  .back-wordmark .trademark { font-size: 9px; top: 0; }
  .tagline {
    font-weight: 400;
    font-size: 13px;
    margin-top: 4px;
    letter-spacing: 0.2px;
  }
  .person {
    text-align: right;
    margin-top: 30px;
  }
  .person-name {
    font-weight: 300;
    font-size: 30px;
  }
  .person-role {
    font-weight: 400;
    font-size: 11px;
    letter-spacing: 5px;
    margin-top: 4px;
  }
  .rule {
    height: 1px;
    background: var(--rule);
    margin: 16px 0 14px;
  }
  .contacts {
    display: flex;
    justify-content: space-between;
    list-style: none;
    font-weight: 300;
    font-size: 12.5px;
  }
  .contacts li { display: flex; align-items: center; gap: 7px; }
  .contacts svg { width: 14px; height: 14px; fill: none; stroke: var(--ink); stroke-width: 1.6; }
</style>
</head>
<body>
<main class="sheet">
  <section class="card card-front" aria-label="Card front">
    <h1 class="front-wordmark">Lodgewell<span class="trademark">™</span></h1>
  </section>

  <section class="card card-back" aria-label="Card back">
    <div class="brand-row">
      <span class="brand-square" aria-hidden="true"></span>
      <div class="brand-text">
        <h2 class="back-wordmark">Lodgewell<span class="trademark">™</span></h2>
        <p class="tagline">Holiday Let Consultants &amp; Management Specialists</p>
      </div>
    </div>

    <div class="person">
      <p class="person-name">Owen Brisk</p>
      <p class="person-role">PRINCIPAL DIRECTOR</p>
    </div>

    <div class="rule"></div>

    <ul class="contacts">
      <li>
        <svg viewBox="0 0 16 16" aria-hidden="true"><rect x="4.5" y="1.5" width="7" height="13" rx="1.5"/><line x1="7" y1="12" x2="9" y2="12"/></svg>
        0487350216
      </li>
      <li>
        <svg viewBox="0 0 16 16" aria-hidden="true"><rect x="1.5" y="3.5" width="13" height="9"/><polyline points="1.5,3.5 8,9 14.5,3.5"/></svg>
        enquiries@lodgewell.com.au
      </li>
      <li>
        <svg viewBox="0 0 16 16" aria-hidden="true"><circle cx="8" cy="8" r="6.5"/><ellipse cx="8" cy="8" rx="3" ry="6.5"/><line x1="1.5" y1="8" x2="14.5" y2="8"/></svg>
        www.lodgewell.com.au
      </li>
    </ul>
  </section>
</main>
</body>
</html>
```